Brighter Than Dawn Home Entertainment

We are a home theater installation company focus on front projection system and home theater surround system. We built highend home theater for people to enjoy movie, sports and gaming on big screen at home.
I'm looking for a dispaly to showcase our work as well as help people build their home theater

Number of Pages Required

3 page

Colors

Designer to choose colors to be used in the design.

Requirements
Must have
• Home Page
• What we do
• Who we are
• Gallery
• Contact Us
Nice to have
• Picture jump out of big screen make a 3D feeling

```html
<!DOCTYPE html>
<html lang="en">
<head>
<meta charset="utf-8">
<title>Home Theater Installation Company</title>
<link href="https://fonts.googleapis.com/css2?family=Montserrat:wght@500;600;700&family=Open+Sans:wght@400;600&display=swap" rel="stylesheet">
<style>
  :root{
    --navy:#0b2e5f;
    --navy-deep:#082349;
    --gold:#a86a0e;
    --ink:#3a3a3a;
    --text:#555;
    --white:#fff;
    --line:#ddd;
  }
  *{box-sizing:border-box;margin:0;padding:0}
  html,body{width:1200px;height:3340px;overflow:hidden;background:var(--white)}
  body{position:relative;font-family:"Open Sans",Arial,sans-serif;color:var(--text)}
  .abs{position:absolute}
  .display{font-family:"Montserrat",Arial,sans-serif}

  /* header */
  .site-header{left:0;top:0;width:1200px;height:110px;background:var(--navy)}
  .brand{left:85px;top:22px;display:flex;align-items:center;gap:16px;color:var(--white)}
  .brand-mark{width:62px;height:62px;background:var(--white)}
  .brand-name{font-family:"Montserrat",sans-serif;font-weight:700;font-size:25px;line-height:28px;text-transform:uppercase}
  .brand-name small{display:block;font-size:17px;line-height:22px}
  .main-nav{right:85px;top:42px;display:flex;gap:38px}
  .main-nav a{color:var(--white);text-decoration:none;font-size:14px;text-transform:uppercase;padding-bottom:6px}
  .main-nav a.active{border-bottom:2px solid var(--white)}

  /* hero */
  .hero-photo{left:0;top:110px;width:792px;height:530px;background:linear-gradient(135deg,#f4f4f4 0%,#e3e3e3 55%,#3a3a3a 85%,#1e1e1e 100%)}
  .hero-panel{left:792px;top:110px;width:408px;height:445px;background:var(--navy)}
  .hero-title{left:837px;top:218px;color:var(--white);font-family:"Montserrat",sans-serif;font-weight:700;font-size:39px;line-height:45px;text-transform:uppercase}

  /* buttons */
  .btn{display:flex;align-items:center;justify-content:center;color:var(--white);background:var(--gold);font-size:13px;font-weight:600;text-transform:uppercase;text-decoration:none;clip-path:polygon(10% 0,90% 0,100% 50%,90% 100%,10% 100%,0 50%)}

  /* what we do */
  .section-title{font-family:"Montserrat",sans-serif;font-weight:600;font-size:36px;color:var(--ink);text-transform:uppercase}
  .wwd-title{left:85px;top:752px}
  .wwd-rule{left:85px;top:798px;width:80px;height:2px;background:var(--ink)}
  .wwd-text{left:85px;top:830px;width:500px;font-size:15.5px;line-height:28px}
  .wwd-btn{left:85px;top:1002px;width:167px;height:38px}
  .wwd-frame{left:637px;top:746px;width:445px;height:278px;border:3px solid var(--navy)}
  .wwd-photo{left:668px;top:777px;width:447px;height:278px;background:linear-gradient(160deg,#6fa3c9 0%,#4a7fb0 40%,#c49a6c 70%,#1f4f9c 100%)}

  /* who we are */
  .wwa-band{left:0;top:1149px;width:1200px;height:598px}
  .wwa-title{left:0;top:1178px;width:1200px;text-align:center}
  .wwa-text{left:222px;top:1706px;width:756px;text-align:center;font-size:15.5px;line-height:28px}
  .wwa-btn{left:519px;top:1854px;width:164px;height:38px}

  /* gallery */
  .gallery-title{left:0;top:1960px;width:1200px;text-align:center}
  .tile{position:absolute}

  /* contact */
  .contact{left:0;top:2793px;width:1200px;height:412px;background:linear-gradient(180deg,#1d3f72 0%,var(--navy) 45%,var(--navy-deep) 100%)}
  .contact-title{left:0;top:2852px;width:1200px;text-align:center;color:var(--white);font-family:"Montserrat",sans-serif;font-weight:600;font-size:36px;text-transform:uppercase}
  .field{background:var(--white);font-size:13px;color:#666;padding:10px 10px}
  .captcha-code{position:absolute;right:18px;top:12px;font-weight:600;color:#333;font-size:13px}
  .submit{left:959px;top:3072px;width:152px;height:42px}

  /* footer */
  .footer-nav{left:0;top:3244px;width:1200px;display:flex;justify-content:center;gap:42px}
  .footer-nav a{color:#555;text-decoration:none;font-size:13px;text-transform:uppercase}
  .copyright{left:0;top:3283px;width:1200px;text-align:center;font-size:13px;color:#555}
</style>
</head>
<body>

<header class="abs site-header">
  <div class="abs brand">
    <span class="brand-mark"></span>
    <span class="brand-name">Home Theater<small>Installation Company</small></span>
  </div>
  <nav class="abs main-nav">
    <a class="active" href="#">Home</a>
    <a href="#">What We Do</a>
    <a href="#">Who We Are</a>
    <a href="#">Gallery</a>
    <a href="#">Contact Us</a>
  </nav>
</header>

<div class="abs hero-photo" role="img" aria-label="Bright white home theater room with projector, large screen and black leather recliners"></div>
<div class="abs hero-panel"></div>
<h1 class="abs hero-title">We are a<br>home theater<br>installation<br>company</h1>

<section>
  <h2 class="abs section-title wwd-title">What We Do</h2>
  <div class="abs wwd-rule"></div>
  <p class="abs wwd-text">Lorem Ipsum is simply dummy text of the printing and typesetting industry. Lorem Ipsum has been the industry's standard dummy text ever since the 1500s, when an unknown printer took a galley of type and scrambled it to make a type specimen book.<br>It has survived not only five centuries, but also the leap into</p>
  <a class="abs btn wwd-btn" href="#">Request a Demo</a>
  <div class="abs wwd-frame"></div>
  <div class="abs wwd-photo" role="img" aria-label="Fans cheering in front of a big screen showing a football match"></div>
</section>

<section>
  <svg class="abs wwa-band" width="1200" height="598" viewBox="0 0 1200 598" role="img" aria-label="Dark private cinema room with large screen and wall lights">
    <defs>
      <linearGradient id="cinema" x1="0" y1="0" x2="0" y2="1">
        <stop offset="0" stop-color="#1a1c24"/>
        <stop offset="0.5" stop-color="#2b3040"/>
        <stop offset="1" stop-color="#101218"/>
      </linearGradient>
    </defs>
    <rect width="1200" height="598" fill="url(#cinema)"/>
    <polygon points="0,0 283,105 917,105 1200,0" fill="#fff"/>
    <polygon points="0,598 283,492 917,492 1200,598" fill="#fff"/>
  </svg>
  <h2 class="abs section-title wwa-title">Who We Are</h2>
  <p class="abs wwa-text">Lorem Ipsum is simply dummy text of the printing and typesetting industry. Lorem Ipsum has been the industry's standard dummy text ever since the 1500s, when an unknown printer took a galley of type and scrambled it to make a type specimen book. It has survived not only five centuries, but also the leap into electronic typesetting, remaining essentially unchanged.</p>
  <a class="abs btn wwa-btn" href="#">Contact Us</a>
</section>

<section>
  <h2 class="abs section-title gallery-title">Gallery</h2>
  <div class="tile" style="left:85px;top:2043px;width:329px;height:205px;background:linear-gradient(180deg,#2a2018,#c9a070 45%,#1a1410)" role="img" aria-label="Home cinema with glowing screen and rows of seats"></div>
  <div class="tile" style="left:434px;top:2043px;width:681px;height:432px;background:linear-gradient(180deg,#3a2c22,#6b5a4a 40%,#7a4a28 75%,#3a2a1c)" role="img" aria-label="Wood-panelled theater room with stage and curtained screen"></div>
  <div class="tile" style="left:85px;top:2270px;width:329px;height:205px;background:linear-gradient(160deg,#8a7a6c,#3a4a7a 45%,#4a3a36)" role="img" aria-label="Living room with wall-mounted screen and sofa"></div>
  <div class="tile" style="left:85px;top:2497px;width:329px;height:205px;background:linear-gradient(180deg,#a0b8c8,#5a4a8a 50%,#b0203a 80%,#e0e0e0)" role="img" aria-label="Gaming desk with multiple monitors and coloured lights"></div>
  <div class="tile" style="left:434px;top:2497px;width:332px;height:205px;background:linear-gradient(180deg,#d8d8d8,#6a6a6a 50%,#1e1e1e)" role="img" aria-label="Lounge with television, speakers and black sofa"></div>
  <div class="tile" style="left:784px;top:2497px;width:331px;height:205px;background:linear-gradient(180deg,#e8e8e8,#c8c8c8 40%,#2a2a2a 55%,#d0d0d0 80%)" role="img" aria-label="Wall-mounted flat screen showing a lit building"></div>
</section>

<section class="abs contact" role="img" aria-label="Dark blue tinted home theater room"></section>
<h2 class="abs contact-title">Contact Us Now</h2>
<div class="abs field" style="left:85px;top:2940px;width:500px;height:172px">Message</div>
<div class="abs field" style="left:617px;top:2940px;width:498px;height:43px">Name</div>
<div class="abs field" style="left:617px;top:3005px;width:498px;height:45px">Email</div>
<div class="abs field" style="left:617px;top:3072px;width:331px;height:42px">Type the code shown<span class="captcha-code">HG845</span></div>
<a class="abs btn submit" href="#">Submit</a>

<footer>
  <nav class="abs footer-nav">
    <a href="#">Home</a>
    <a href="#">What We Do</a>
    <a href="#">Who We Are</a>
    <a href="#">Gallery</a>
    <a href="#">Contact Us</a>
  </nav>
  <p class="abs copyright">© 2018 DOMAIN. All rights reserved.</p>
</footer>

</body>
</html>
```